Toplyx Landing Page

We need a web design for an e-commerce website that allows user to sell and buy products from other users.
We would like the website design to:
- show all posted items tiled across the webpage that dynamically resizes depending on the size of the user's screen and appears endless so that users can keep on scrolling down.
- Show a map button where user can choose the area where they want to filter by.
- show search field
- drop down button to choose product category from
- show under each item a requested price and a current highest offer by prospect buyers.

We have attached a sample of a mockup that we have done before but did not quite like the design, however it will give you an idea of what the posted item will look like. The "share" and "heart" logo can be removed and can appear when user hover their mouse across the picture or if user is using mobile when they click on the item.

Ideally we would like the design to be tidy, flawless and very user friendly with blue themed color.

Industry/Entity Type

E-Commerce

```html
<!DOCTYPE html>
<html lang="en">
<head>
<meta charset="utf-8">
<title>Toplyx Landing Page</title>
<link href="https://fonts.googleapis.com/css2?family=Open+Sans:wght@400;600;700&family=Arimo:wght@400;700&display=swap" rel="stylesheet">
<style>
:root{
  --navy:#2f3d50;
  --navy-dark:#283546;
  --yellow:#f0c30f;
  --white:#ffffff;
  --text:#3b3b3b;
  --muted:#9a9a9a;
  --line:#e4e4e4;
  --hero-a:#6d7c8c;
  --hero-b:#a8b3bd;
}
*{box-sizing:border-box;margin:0;padding:0}
html,body{width:810px;height:1200px;overflow:hidden;background:var(--white)}
body{position:relative;font-family:"Open Sans",sans-serif;color:var(--text)}

.site-header{position:absolute;top:0;left:0;width:810px;height:64px;background:var(--navy);border-bottom:1px solid #45556a}
.brand{position:absolute;left:89px;top:14px;display:flex;align-items:center;gap:6px}
.brand-dot{width:22px;height:22px;border-radius:50%;background:var(--yellow)}
.brand-name{font-family:"Open Sans",sans-serif;font-weight:700;font-size:25px;color:var(--white);letter-spacing:.3px}
.nav-link{position:absolute;top:27px;font-family:"Arimo",sans-serif;font-size:10px;color:var(--white)}
.nav-btn{position:absolute;top:20px;height:23px;background:var(--yellow);color:var(--white);font-family:"Arimo",sans-serif;font-size:10px;display:flex;align-items:center;justify-content:center;gap:8px}

.hero{position:absolute;top:64px;left:0;width:810px;height:326px;background:linear-gradient(160deg,var(--hero-b) 0%,var(--hero-a) 55%,#4f5d6c 100%)}
.hero-title{position:absolute;top:118px;left:0;width:810px;text-align:center;font-family:"Arimo",sans-serif;font-weight:700;font-size:36px;letter-spacing:2px;color:var(--white);text-shadow:0 2px 4px rgba(0,0,0,.35)}
.search-panel{position:absolute;left:170px;top:178px;width:470px;height:53px;background:rgba(255,255,255,.3)}
.search-input{position:absolute;left:10px;top:10px;width:338px;height:32px;background:var(--white);display:flex;align-items:center;gap:6px;padding-left:9px;font-size:7px;color:#777}
.search-btn{position:absolute;left:360px;top:10px;width:81px;height:32px;background:var(--yellow);color:var(--white);font-weight:700;font-size:11px;display:flex;align-items:center;justify-content:center}
.hero-next{position:absolute;left:728px;top:142px}

.trending{position:absolute;top:390px;left:0;width:810px;height:48px;background:var(--yellow);display:flex;align-items:center;padding-left:89px}
.trending-label{font-weight:700;font-size:12.5px;color:var(--white);letter-spacing:.8px;padding-right:22px;margin-right:0;border-right:1px solid rgba(255,255,255,.35);height:30px;display:flex;align-items:center}
.trending-item{font-size:10px;color:var(--white);letter-spacing:.4px;padding:0 14px;height:30px;display:flex;align-items:center;border-right:1px solid rgba(255,255,255,.35)}
.trending-item:last-child{border-right:none}

.featured-title{position:absolute;top:464px;left:0;width:810px;text-align:center;font-weight:700;font-size:16px;color:var(--text)}
.featured-title span{color:var(--yellow)}
.featured-intro{position:absolute;top:495px;left:140px;width:530px;text-align:center;font-family:"Arimo",sans-serif;font-size:7.2px;line-height:13.5px;color:#555}

.product-card{position:absolute;width:192px;height:222px;background:var(--white);border:1px solid var(--line)}
.product-dome{position:absolute;left:47px;top:-36px;width:96px;height:36px;border:1px solid var(--line);border-bottom:none;border-radius:48px 48px 0 0;background:var(--white)}
.product-image{position:absolute;left:46px;top:-2px;width:100px;height:88px;border-radius:4px;background:linear-gradient(180deg,#e7eaee,#c4cad1)}
.product-name{position:absolute;top:95px;left:0;width:100%;text-align:center;font-weight:600;font-size:12.5px;color:var(--text)}
.product-desc{position:absolute;top:122px;left:10px;width:172px;text-align:center;font-family:"Arimo",sans-serif;font-size:7px;line-height:16px;color:var(--muted)}
.price{position:absolute;top:178px;width:70px;height:25px;color:var(--white);font-weight:700;font-size:6.6px;text-align:center;line-height:10px;padding-top:3px;letter-spacing:.3px}
.price-offer{left:20px;background:var(--yellow)}
.price-asking{left:101px;background:var(--navy)}

.site-footer{position:absolute;top:1094px;left:0;width:810px;height:106px;background:var(--navy)}
.social{position:absolute;top:24px;left:103px;display:flex;gap:6px}
.social span{width:22px;height:22px;border:1.5px solid var(--white);border-radius:50%}
.newsletter-label{position:absolute;left:268px;top:24px;font-size:13.5px;color:var(--white)}
.newsletter-divider{position:absolute;left:346px;top:26px;width:1px;height:26px;background:#56667b}
.newsletter-text{position:absolute;left:358px;top:26px;font-family:"Arimo",sans-serif;font-size:6.6px;line-height:13px;color:var(--white)}
.newsletter-field{position:absolute;left:541px;top:23px;width:169px;height:28px;background:#eef0f2;display:flex;align-items:center;padding-left:7px;gap:6px;font-size:5.8px;color:#8c8c8c}
.newsletter-field svg.go{position:absolute;right:8px;top:9px}
.footer-rule{position:absolute;left:98px;top:64px;width:614px;height:1px;background:#45556a}
.copyright{position:absolute;top:81px;left:0;width:810px;text-align:center;font-family:"Arimo",sans-serif;font-size:7.2px;color:var(--white)}
</style>
</head>
<body>

<header class="site-header">
  <div class="brand"><span class="brand-dot"></span><span class="brand-name">Toplyx</span></div>
  <span class="nav-link" style="left:322px">SIGN UP</span>
  <span class="nav-link" style="left:390px">LOG IN</span>
  <span class="nav-link" style="left:451px">ABOUT US</span>
  <span class="nav-btn" style="left:512px;width:66px">MAP</span>
  <span class="nav-btn" style="left:586px;width:135px">PRODUCT CATEGORY
    <svg width="8" height="5" viewBox="0 0 8 5"><path d="M0 0h8L4 5z" fill="#fff"/></svg>
  </span>
</header>

<section class="hero" role="img" aria-label="Blurred crowd of shoppers crossing a busy city street">
  <h1 class="hero-title">FIND YOUR FOVORITE ITEM</h1>
  <form class="search-panel">
    <div class="search-input">
      <svg width="10" height="10" viewBox="0 0 10 10"><circle cx="4" cy="4" r="3" fill="none" stroke="#999" stroke-width="1.4"/><path d="M6.2 6.2L9 9" stroke="#999" stroke-width="1.6"/></svg>
      START YOUR SEARCH.........
    </div>
    <div class="search-btn">SEARCH</div>
  </form>
  <svg class="hero-next" width="44" height="44" viewBox="0 0 44 44"><circle cx="22" cy="22" r="20" fill="rgba(255,255,255,.12)" stroke="rgba(255,255,255,.45)" stroke-width="2"/><path d="M17 13l12 9-12 9z" fill="rgba(255,255,255,.5)"/></svg>
</section>

<nav class="trending">
  <span class="trending-label">TRENDING NOW!</span>
  <span class="trending-item">Sorin Lumo</span>
  <span class="trending-item">Vista 27</span>
  <span class="trending-item">Phonix 6</span>
  <span class="trending-item">Brewmatic Coffee</span>
  <span class="trending-item">Crispo Chips</span>
  <span class="trending-item">more...</span>
</nav>

<h2 class="featured-title">FEATURED <span>PRODUCTS</span></h2>
<p class="featured-intro">Tile Market is the first auction site of its kind. The innovative concept of 'squares' means that the price is constantly adapting to your chances of winning making it impossible for you to pay more than the odds</p>

<article class="product-card" style="left:89px;top:570px">
  <div class="product-dome"></div>
  <div class="product-image" role="img" aria-label="Two desktop computers with widescreen displays"></div>
  <h3 class="product-name">VISTA 27</h3>
  <p class="product-desc">Sed ut perspiciatis unde omnis iste natus error sit accusantium doloremque laudantium, totam qsunt explicabo.</p>
  <div class="price price-offer">OFFER PRICE<br>$320</div>
  <div class="price price-asking">ASKING PRICE<br>$799</div>
</article>

<article class="product-card" style="left:310px;top:570px">
  <div class="product-dome"></div>
  <div class="product-image" role="img" aria-label="Black smartphone shown from front and side"></div>
  <h3 class="product-name">PHONIX 6</h3>
  <p class="product-desc">Sed ut perspiciatis unde omnis iste natus error sit accusantium doloremque laudantium, totam qsunt explicabo.</p>
  <div class="price price-offer">OFFER PRICE<br>$320</div>
  <div class="price price-asking">ASKING PRICE<br>$799</div>
</article>

<article class="product-card" style="left:530px;top:570px">
  <div class="product-dome"></div>
  <div class="product-image" role="img" aria-label="Silver laptop shown open and closed"></div>
  <h3 class="product-name">VISTA 27</h3>
  <p class="product-desc">Sed ut perspiciatis unde omnis iste natus error sit accusantium doloremque laudantium, totam qsunt explicabo.</p>
  <div class="price price-offer">OFFER PRICE<br>$320</div>
  <div class="price price-asking">ASKING PRICE<br>$799</div>
</article>

<article class="product-card" style="left:89px;top:860px">
  <div class="product-dome"></div>
  <div class="product-image" role="img" aria-label="White wall charger with USB cable"></div>
  <h3 class="product-name">USB</h3>
  <p class="product-desc">Sed ut perspiciatis unde omnis iste natus error sit accusantium doloremque laudantium, totam qsunt explicabo.</p>
  <div class="price price-offer">OFFER PRICE<br>$320</div>
  <div class="price price-asking">ASKING PRICE<br>$799</div>
</article>

<article class="product-card" style="left:310px;top:860px">
  <div class="product-dome"></div>
  <div class="product-image" role="img" aria-label="Black smartphone shown from front and side"></div>
  <h3 class="product-name">VISTA 27</h3>
  <p class="product-desc">Sed ut perspiciatis unde omnis iste natus error sit accusantium doloremque laudantium, totam qsunt explicabo.</p>
  <div class="price price-offer">OFFER PRICE<br>$320</div>
  <div class="price price-asking">ASKING PRICE<br>$799</div>
</article>

<article class="product-card" style="left:530px;top:860px">
  <div class="product-dome"></div>
  <div class="product-image" role="img" aria-label="Pink smartphone shown from front and back" style="background:linear-gradient(180deg,#f1dbe4,#d66b95)"></div>
  <h3 class="product-name">SORIN LUMO</h3>
  <p class="product-desc">Sed ut perspiciatis unde omnis iste natus error sit accusantium doloremque laudantium, totam qsunt explicabo.</p>
  <div class="price price-offer">OFFER PRICE<br>$320</div>
  <div class="price price-asking">ASKING PRICE<br>$799</div>
</article>

<footer class="site-footer">
  <div class="social"><span></span><span></span><span></span><span></span><span></span></div>
  <span class="newsletter-label">NewsLetter :</span>
  <span class="newsletter-divider"></span>
  <p class="newsletter-text">In venenatis neque a eros laoreet eu placerat erat suscipit.<br>Fusce cursus, erat ut scelerisque condimentum</p>
  <div class="newsletter-field">
    <svg width="14" height="10" viewBox="0 0 14 10"><rect x=".5" y=".5" width="13" height="9" fill="none" stroke="#999"/><path d="M.5.5L7 6l6.5-5.5" fill="none" stroke="#999"/></svg>
    Enter Your Email Address :
    <svg class="go" width="6" height="10" viewBox="0 0 6 10"><path d="M1 1l4 4-4 4" fill="none" stroke="#999" stroke-width="1.2"/></svg>
  </div>
  <div class="footer-rule"></div>
  <p class="copyright">© Copy Rights 2014 Toplyx.All Rights Reserved</p>
</footer>

</body>
</html>
```